Dr Maren Holt, Orthopaedic Hand Surgeon

I am an orthopaedic hand surgeon and need business cards that reflect the surgery I do. I operate on bones, ligaments, tendons, and soft tissues. I can do microsurgery (surgery under an operating microscope) - including connecting ends of cut nerves and arteries in the fingers together. As an orthopaedic surgeon, I also fix fractures and manage orthopaedic trauma in the rest of the body. I favour black as a colour, and have some pictures of hand X-rays that you can use in the design, if you think that would look good (feel free to crop).

Hi all. Thank you for all your submissions so far. Please note that I have updated my project brief. I would like to emphasise that use of the logos that I have provided is optional, and if used, I would very much prefer the logo not to dominate the card, but add to the overall aesthetic of the card. Warm regards, Maren

Target Market(s)

Referring medical practitioners, hand therapists, patients

Industry/Entity Type

Healthcare

Contact Information for Business Card

Dr Maren Holt
Orthopaedic Hand Surgeon
MBBS BSc (Med), MIntPH (Merit), GWELN (Ortho), MIvroE

Font styles to use
Serif

Colors

Designer to choose colors to be used in the design.

Requirements
Must have
• Space for:
• 2 addresses (a PO Box Address and a consulting suite address) - to be confirmed
• 1 phone number - to be confirmed
Nice to have
• Please choose one of the GWELN logos (I included 3 - colour, black reverse, and greyscale); if you include this in the design, IT SHOULD NOT DOMINATE THE CARD, but be smaller and more discreet.
• I have also attached the MIvroE logo (colour and greyscale); if you choose to include this in the design, IT SHOULD NOT DOMINATE THE CARD, but be smaller and more discreet.
• I would love to be able to update details on the card as time goes on, and thus would like to own the template for the card as well.
• Also I would love discussion with regard to any changes on the card, if I am not completely happy with the design, and would like to discuss things such as ease of printing, finish on the cards (matte, polish) etc.
Should not have
• I don't like the card to look too crowded

```html
<!DOCTYPE html>
<html lang="en">
<head>
<meta charset="utf-8">
<title>Dr Maren Holt – Orthopaedic Hand Surgeon</title>
<link rel="stylesheet" href="https://fonts.googleapis.com/css2?family=Tinos&display=swap">
<style>
  :root {
    --card-black: #000000;
    --accent-cyan: #3ccbee;
    --text-white: #ffffff;
    --xray-light: rgba(190, 190, 190, 0.32);
    --xray-mid: rgba(120, 120, 120, 0.16);
    --crest-fill: #c8a23c;
  }
  html, body {
    margin: 0;
    padding: 0;
    width: 1200px;
    height: 686px;
    overflow: hidden;
    background: var(--card-black);
  }
  .business-card {
    position: relative;
    width: 1200px;
    height: 686px;
    background: var(--card-black);
    overflow: hidden;
    font-family: "Tinos", "Times New Roman", serif;
    color: var(--text-white);
  }
  .xray-hand {
    position: absolute;
  }
  .xray-hand--top-left {
    left: -40px;
    top: -40px;
    width: 560px;
    height: 360px;
    background: radial-gradient(ellipse at 30% 35%, var(--xray-light) 0%, var(--xray-mid) 45%, transparent 72%);
    transform: rotate(18deg);
  }
  .xray-hand--bottom-right {
    right: -60px;
    bottom: -60px;
    width: 600px;
    height: 360px;
    background: radial-gradient(ellipse at 65% 60%, var(--xray-light) 0%, var(--xray-mid) 45%, transparent 72%);
    transform: rotate(-14deg);
  }
  .side-bars {
    position: absolute;
    inset: 0;
  }
  .membership-mark {
    position: absolute;
    left: 714px;
    top: 32px;
    display: flex;
    align-items: center;
    gap: 16px;
  }
  .membership-mark__square {
    width: 84px;
    height: 84px;
    background: var(--crest-fill);
  }
  .membership-mark__text {
    color: var(--accent-cyan);
    font-weight: 400;
    line-height: 1.1;
  }
  .membership-mark__acronym {
    display: block;
    font-size: 48px;
  }
  .membership-mark__fellow {
    display: block;
    font-size: 17px;
  }
  .identity {
    position: absolute;
    left: 0;
    right: 0;
    top: 264px;
    text-align: center;
    font-size: 31px;
    line-height: 41px;
  }
  .identity p { margin: 0; }
  .contact-row {
    position: absolute;
    left: 0;
    right: 0;
    top: 476px;
  }
  .contact-item {
    position: absolute;
    width: 240px;
    margin-left: -120px;
    text-align: center;
    font-size: 23px;
  }
  .contact-item svg {
    display: block;
    margin: 0 auto 24px;
  }
  .contact-item--address-one { left: 274px; }
  .contact-item--phone { left: 591px; }
  .contact-item--address-two { left: 923px; }
</style>
</head>
<body>
<div class="business-card">
  <div class="xray-hand xray-hand--top-left" role="img" aria-label="X-ray of a hand with fingers reaching down from the top left"></div>
  <div class="xray-hand xray-hand--bottom-right" role="img" aria-label="X-ray of a hand with fingers reaching up from the bottom right"></div>

  <svg class="side-bars" width="1200" height="686" viewBox="0 0 1200 686" aria-hidden="true">
    <polygon points="0,34 31,58 31,628 0,652" fill="var(--accent-cyan)"/>
    <polygon points="1200,34 1169,58 1169,628 1200,652" fill="var(--accent-cyan)"/>
  </svg>

  <div class="membership-mark">
    <div class="membership-mark__square"></div>
    <div class="membership-mark__text">
      <span class="membership-mark__acronym">GWELN</span>
      <span class="membership-mark__fellow">Fellow of the Northvale College of Surgeons</span>
    </div>
  </div>

  <div class="identity">
    <p class="identity__name">Dr Maren Holt</p>
    <p class="identity__role">Orthopaedic Hand Surgeon</p>
    <p class="identity__credentials">MBBS BSc (Med), MIntPH (Merit), GWELN (Ortho), MIvroE</p>
  </div>

  <div class="contact-row">
    <div class="contact-item contact-item--address-one">
      <svg width="56" height="54" viewBox="0 0 56 54" aria-hidden="true">
        <polygon points="28,2 54,22 50,26 28,9 6,26 2,22" fill="var(--accent-cyan)"/>
        <rect x="40" y="4" width="6" height="12" fill="var(--accent-cyan)"/>
        <path d="M9 24 L28 10 L47 24 V52 H9 Z M15 30 V38 H25 V30 Z M31 30 V38 H41 V30 Z M22 42 V52 H34 V42 Z" fill="var(--accent-cyan)" fill-rule="evenodd"/>
      </svg>
      Address 1
    </div>
    <div class="contact-item contact-item--phone">
      <svg width="56" height="54" viewBox="0 0 56 54" aria-hidden="true">
        <path d="M4 18 C4 8 52 8 52 18 V24 H40 V17 H16 V24 H4 Z" fill="var(--accent-cyan)"/>
        <path d="M14 24 H42 L50 46 V52 H6 V46 Z" fill="var(--accent-cyan)"/>
        <circle cx="28" cy="38" r="8" fill="var(--card-black)"/>
        <circle cx="28" cy="38" r="3" fill="var(--accent-cyan)"/>
      </svg>
      Phone Number
    </div>
    <div class="contact-item contact-item--address-two">
      <svg width="56" height="54" viewBox="0 0 56 54" aria-hidden="true">
        <polygon points="28,2 54,22 50,26 28,9 6,26 2,22" fill="var(--accent-cyan)"/>
        <rect x="40" y="4" width="6" height="12" fill="var(--accent-cyan)"/>
        <path d="M9 24 L28 10 L47 24 V52 H9 Z M15 30 V38 H25 V30 Z M31 30 V38 H41 V30 Z M22 42 V52 H34 V42 Z" fill="var(--accent-cyan)" fill-rule="evenodd"/>
      </svg>
      Address 2
    </div>
  </div>
</div>
</body>
</html>
```